Student Card

we are college and require a student card which we issue on enlroment to students, just like a univeristy.

Baisic information need to be placed is:
Student photo
student ID
date of birth
exp date

our college contact details on the rear
its a tool for branding so its important the theme is in line with our colours and logo, please view our website www.hartwellcollege.net.au

Industry/Entity Type

College

```html
<!DOCTYPE html>
<html lang="en">
<head>
<meta charset="utf-8">
<title>Hartwell College Student Card</title>
<link href="https://fonts.googleapis.com/css2?family=Jost:wght@300;400;500;600&display=swap" rel="stylesheet">
<style>
  :root {
    --page: #e6e7ea;
    --card-white: #f3f4fa;
    --sky: #56bdeb;
    --sky-light: #8fd5f3;
    --navy: #0d4ea8;
    --navy-deep: #0a3f8f;
    --rule: #3aa9e6;
    --frame: #ffffff;
    --photo-fill: #c3c9e4;
    --text-light: #ffffff;
  }
  * { box-sizing: border-box; margin: 0; padding: 0; }
  html, body {
    width: 1200px;
    height: 1013px;
    overflow: hidden;
    background: var(--page);
    font-family: "Jost", "Century Gothic", sans-serif;
  }
  .student-card {
    position: absolute;
    left: 100px;
    top: 220px;
    width: 1000px;
    height: 572px;
    background: var(--card-white);
    overflow: hidden;
    box-shadow: 0 6px 20px rgba(0,0,0,0.18);
  }
  .side-column {
    position: absolute;
    left: 0; top: 75px;
    width: 232px; height: 497px;
    background: linear-gradient(160deg, var(--sky-light), var(--sky) 60%, #3eaee6);
  }
  .accent-bar {
    position: absolute;
    left: 232px; top: 0;
    width: 22px; height: 160px;
    background: var(--navy);
  }
  .info-rule {
    position: absolute;
    left: 254px; top: 140px;
    width: 746px; height: 8px;
    background: var(--rule);
  }
  .info-panel {
    position: absolute;
    left: 232px; top: 148px;
    width: 768px; height: 424px;
    background: var(--navy);
  }
  .panel-photo {
    position: absolute;
    left: 232px; top: 148px;
    width: 768px; height: 424px;
    background: radial-gradient(ellipse at 45% 65%, rgba(120,150,210,0.28), rgba(13,78,168,0) 60%);
  }
  .photo-frame {
    position: absolute;
    left: 88px; top: 128px;
    width: 284px; height: 342px;
    background: var(--frame);
    border-radius: 12px;
    padding: 14px;
  }
  .photo-slot {
    width: 100%; height: 100%;
    background: linear-gradient(180deg, #cdd2ea, var(--photo-fill));
    border-radius: 4px;
  }
  .college-mark {
    position: absolute;
    right: 52px; top: 52px;
    display: flex;
    flex-direction: column;
    align-items: center;
    gap: 6px;
  }
  .college-mark .seal {
    width: 34px; height: 34px;
    border-radius: 50%;
    background: var(--navy);
  }
  .college-mark .college-name {
    font-weight: 500;
    font-size: 17px;
    color: var(--navy);
    letter-spacing: 1px;
    text-transform: uppercase;
  }
  .card-details {
    position: absolute;
    right: 66px; top: 192px;
    text-align: right;
    color: var(--text-light);
    font-size: 36px;
    line-height: 42px;
  }
  .card-details .strong { font-weight: 600; }
  .card-details .light { font-weight: 300; }
  .card-details .web {
    margin-top: 22px;
    font-size: 20px;
    line-height: 24px;
    font-weight: 400;
    letter-spacing: 0.5px;
  }
</style>
</head>
<body>
  <div class="student-card">
    <div class="side-column"></div>
    <div class="info-panel"></div>
    <div class="panel-photo" role="img" aria-label="Faint background photo of students on campus"></div>
    <div class="info-rule"></div>
    <div class="accent-bar"></div>

    <div class="photo-frame">
      <div class="photo-slot" role="img" aria-label="Student photo"></div>
    </div>

    <div class="college-mark">
      <span class="seal"></span>
      <span class="college-name">Hartwell College</span>
    </div>

    <div class="card-details">
      <p class="strong">STUDENT</p>
      <p><span class="light">FIRST NAME</span> <span class="strong">SURNAME</span></p>
      <p class="strong">DD/MM/YYYY</p>
      <p class="light">EXP DATE</p>
      <p class="web">www.hartwellcollege.net.au</p>
    </div>
  </div>
</body>
</html>
```